Brenna's Wine Label Design

Design for a wine bottle label. It'Is for A Dog Bar. This bar is upscale, so I am going for an elegant look
Here is what I am requesting.
1.Label to fit a wine bottle 4" Wide x 5" Length
1. Black Matte or Slate if you if you are having trouble with colors
2. The writing done in Gold Foil
3. Please consider the what the logo looks like- also it has a copy write on the art. If you can insert that it would be nicel
4. Please have print the says the "Pup Warden's Pick"
5. Please Incorporate Saltmere Bay Florida
www.brennacastavelt.example and 555-318-9062
5. Product de France
4. Please incorporate the photo of the dog attached
6. I have added a couple of example label photos to give you an idea of the feel of the look I am seeking
7.One Type of wine is Chardonnay
8.One type of wine is Pinot Noir
8. Notice the image with the dog paw incorporate in the scroll work. Love that!

Target Market(s)

Dog and Upscale Wine lovers

Font styles to use
Decorative
Script

Requirements
Must have
• See Project Description
Nice to have
• Copy right symbol after logo

```html
<!DOCTYPE html>
<html lang="en">
<head>
<meta charset="utf-8">
<title>Brenna's Wine Label – Chardonnay</title>
<link href="https://fonts.googleapis.com/css2?family=Cinzel:wght@400;600&family=Pinyon+Script&display=swap" rel="stylesheet">
<style>
  :root {
    --page: #ffffff;
    --label: #080808;
    --gold: #e2b544;
    --gold-light: #f6df8e;
    --gold-deep: #a97b1c;
  }
  html, body {
    margin: 0;
    padding: 0;
    width: 1200px;
    height: 1187px;
    overflow: hidden;
    background: var(--page);
  }
  .canvas {
    position: relative;
    width: 1200px;
    height: 1187px;
  }
  .wine-label {
    position: absolute;
    left: 202px;
    top: 93px;
    width: 795px;
    height: 1000px;
    background: var(--label);
    color: var(--gold);
    font-family: "Cinzel", serif;
    text-align: center;
  }
  .crest {
    position: absolute;
    left: 50%;
    top: 40px;
    width: 206px;
    height: 206px;
    margin-left: -103px;
    border-radius: 50%;
    background: radial-gradient(circle at 40% 35%, var(--gold-light), var(--gold) 55%, var(--gold-deep));
    box-shadow: 0 0 0 3px var(--label), 0 0 0 5px var(--gold);
  }
  .scrollwork {
    position: absolute;
    left: 18px;
    right: 18px;
    height: 110px;
    background: radial-gradient(ellipse 50% 40% at 50% 55%, rgba(226,181,68,0.55), rgba(169,123,28,0.18) 65%, rgba(8,8,8,0) 100%);
  }
  .scrollwork--top { top: 195px; }
  .scrollwork--bottom { top: 822px; }
  .brand-name {
    position: absolute;
    left: 0; right: 0;
    top: 318px;
    margin: 0;
    font-family: "Pinyon Script", cursive;
    font-size: 76px;
    line-height: 90px;
    font-weight: 400;
    color: var(--gold);
  }
  .brand-name sup {
    font-family: "Cinzel", serif;
    font-size: 18px;
    vertical-align: 38px;
    margin-left: 4px;
  }
  .brand-sub {
    position: absolute;
    left: 0; right: 0;
    top: 416px;
    margin: 0;
    font-size: 30px;
    line-height: 36px;
    font-weight: 600;
    letter-spacing: 2px;
  }
  .rule {
    position: absolute;
    left: 55px;
    width: 685px;
    height: 16px;
  }
  .rule--upper { top: 479px; }
  .rule--lower { top: 655px; }
  .cuvee {
    position: absolute;
    left: 0; right: 0;
    top: 504px;
    margin: 0;
    font-size: 26px;
    line-height: 32px;
    font-weight: 400;
    letter-spacing: 1px;
  }
  .varietal {
    position: absolute;
    left: 0; right: 0;
    top: 545px;
    margin: 0;
    font-size: 76px;
    line-height: 90px;
    font-weight: 400;
    letter-spacing: 2px;
    color: var(--gold-light);
  }
  .details {
    position: absolute;
    left: 0; right: 0;
    top: 712px;
    margin: 0;
    font-size: 16px;
    line-height: 20px;
    letter-spacing: 1px;
    color: var(--gold-deep);
  }
  .details span { display: block; }
  .details .origin { font-size: 20px; line-height: 24px; }
  .details .town { font-size: 17px; line-height: 22px; }
</style>
</head>
<body>
<main class="canvas">
  <section class="wine-label">
    <div class="crest" role="img" aria-label="Brenna's crest medallion"></div>
    <div class="scrollwork scrollwork--top" role="img" aria-label="Gold scroll ornament with paw prints"></div>

    <h1 class="brand-name">Brenna Castavelt<sup>®</sup></h1>
    <p class="brand-sub">Hound Hall</p>

    <svg class="rule rule--upper" viewBox="0 0 685 16" aria-hidden="true">
      <line x1="8" y1="8" x2="677" y2="8" stroke="#e2b544" stroke-width="2.5"/>
      <circle cx="8" cy="8" r="7" fill="#e2b544"/>
      <circle cx="677" cy="8" r="7" fill="#e2b544"/>
    </svg>

    <p class="cuvee">Pup Warden's Pick</p>
    <h2 class="varietal">Chardonnay</h2>

    <svg class="rule rule--lower" viewBox="0 0 685 16" aria-hidden="true">
      <line x1="8" y1="8" x2="677" y2="8" stroke="#e2b544" stroke-width="2.5"/>
      <circle cx="8" cy="8" r="7" fill="#e2b544"/>
      <circle cx="677" cy="8" r="7" fill="#e2b544"/>
    </svg>

    <p class="details">
      <span class="origin">Product de France</span>
      <span class="town">Saltmere Bay Florida</span>
      <span>www.brennacastavelt.example</span>
      <span>555-318-9062</span>
    </p>

    <div class="scrollwork scrollwork--bottom" role="img" aria-label="Gold scroll ornament with paw prints"></div>
  </section>
</main>
</body>
</html>
```